Vemtra Group: Business Card for a high end technology company

We need a cool new design for our business cards using our cloud logo. We are a technology consulting business. We pride ourselves on be the best of the best. We mainly focus on cloud solutions and managed services. We need a business card that sets us apart from the other technology companies in the area and allows us to stand out.

Target Market(s)

Technology departments, CIO, CEOs, and Information Technology Staff.

Industry/Entity Type

Information Technology

Contact Information for Business Card

Must have the logo and our name.
Must have employee name, email address, office phone, cell phone and website.
Need to have all info on one side a cool design on backside.

Font styles to use
Serif
Sans Serif

Requirements
Must have
• Must have the logo and our name.
• Must have employee name, email address, office phone, cell phone and website.
• Need to have all info on one side a cool design on back side.
• Must be a crisp clean design, not too busy or confusing.

```html
<!DOCTYPE html>
<html lang="en">
<head>
<meta charset="utf-8">
<title>Vemtra Group — Business Card</title>
<link href="https://fonts.googleapis.com/css2?family=Arimo:wght@400;700&family=Montserrat:wght@500&display=swap" rel="stylesheet">
<style>
  :root {
    --page-bg: #e6e6e6;
    --card-bg: #ffffff;
    --brand-blue: #2268b3;
    --sky-blue: #2a9bf0;
    --charcoal: #353233;
    --wordmark: #333333;
    --contact-text: #f2f2f2;
    --icon-bg: #ffffff;
  }
  * { margin: 0; padding: 0; box-sizing: border-box; }
  html, body {
    width: 1189px;
    height: 1200px;
    overflow: hidden;
    background: var(--page-bg);
  }
  .sheet {
    position: relative;
    width: 1189px;
    height: 1200px;
  }
  .card-slot {
    position: absolute;
    left: 136px;
    width: 917px;
    height: 524px;
    box-shadow: 0 6px 14px rgba(0,0,0,0.25);
  }
  .card-slot--front { top: 60px; }
  .card-slot--back { top: 617px; }
  .card {
    position: absolute;
    top: 0;
    left: 0;
    width: 1124px;
    height: 642px;
    background: var(--card-bg);
    overflow: hidden;
    transform: scale(0.8159);
    transform-origin: top left;
  }
  .card__wave {
    position: absolute;
    left: 0;
    top: 0;
    width: 1124px;
    height: 642px;
  }
  .wave-band { fill: var(--brand-blue); }
  .wave-base { fill: var(--charcoal); }

  .brand-dot {
    position: absolute;
    border-radius: 50%;
    background: var(--sky-blue);
  }
  .brand-dot--front { left: 278px; top: 105px; width: 90px; height: 90px; }
  .brand-dot--back { left: 483px; top: 175px; width: 150px; height: 150px; }

  .brand-name {
    position: absolute;
    font-family: "Montserrat", sans-serif;
    font-weight: 500;
    line-height: 1;
    color: var(--wordmark);
    white-space: nowrap;
  }
  .brand-name--front {
    left: 103px;
    top: 266px;
    font-size: 78px;
  }
  .brand-name--back {
    left: 0;
    right: 0;
    top: 445px;
    text-align: center;
    font-size: 124px;
  }

  .holder-name {
    position: absolute;
    right: 66px;
    top: 194px;
    font-family: "Arimo", sans-serif;
    font-weight: 700;
    font-size: 56px;
    line-height: 1;
    letter-spacing: 1px;
    color: var(--brand-blue);
    white-space: nowrap;
  }

  .contact-list {
    position: absolute;
    right: 68px;
    top: 378px;
    list-style: none;
    font-family: "Arimo", sans-serif;
    font-size: 26px;
    color: var(--contact-text);
    white-space: nowrap;
  }
  .contact-list__item {
    display: flex;
    justify-content: flex-end;
    align-items: center;
    height: 44.5px;
    gap: 29px;
  }
  .contact-icon {
    width: 22px;
    height: 22px;
    flex: none;
  }
  .contact-icon .tile { fill: var(--icon-bg); }
  .contact-icon .glyph { fill: var(--charcoal); }
  .contact-icon .glyph-line { fill: none; stroke: var(--icon-bg); stroke-width: 1.4; }
</style>
</head>
<body>
<main class="sheet">

  <section class="card-slot card-slot--front" aria-label="Card front">
    <div class="card">
      <svg class="card__wave" viewBox="0 0 1124 642" aria-hidden="true">
        <path class="wave-band" d="M0,326 C120,358 200,385 300,383 C500,378 700,290 880,290 C980,290 1060,330 1124,366 L1124,372 C1060,335 980,300 880,300 C700,300 500,440 300,435 C180,432 80,410 0,393 Z"/>
        <path class="wave-base" d="M0,393 C80,410 180,432 300,435 C500,440 700,300 880,300 C980,300 1060,335 1124,372 L1124,642 L0,642 Z"/>
      </svg>

      <span class="brand-dot brand-dot--front"></span>
      <div class="brand-name brand-name--front">Vemtra Group</div>

      <h1 class="holder-name">Daniel Reyes</h1>

      <ul class="contact-list">
        <li class="contact-list__item">
          <span>555.019.3620</span>
          <svg class="contact-icon" viewBox="0 0 22 22" aria-label="Office phone">
            <rect class="tile" width="22" height="22"/>
            <path class="glyph" d="M4 8 Q11 3 18 8 L17 10 L14 9 L14 8 Q11 7 8 8 L8 9 L5 10 Z"/>
            <rect class="glyph" x="6" y="11" width="10" height="7"/>
          </svg>
        </li>
        <li class="contact-list__item">
          <span>555.019.7714</span>
          <svg class="contact-icon" viewBox="0 0 22 22" aria-label="Cell phone">
            <rect class="tile" width="22" height="22"/>
            <rect class="glyph" x="7" y="3" width="8" height="16" rx="1"/>
            <rect class="tile" x="8.5" y="5" width="5" height="9"/>
          </svg>
        </li>
        <li class="contact-list__item">
          <span>info@vemtragroup.com</span>
          <svg class="contact-icon" viewBox="0 0 22 22" aria-label="Email">
            <rect class="tile" width="22" height="22"/>
            <rect class="glyph" x="4" y="6" width="14" height="10"/>
            <path class="glyph-line" d="M4.5 6.5 L11 12 L17.5 6.5"/>
          </svg>
        </li>
        <li class="contact-list__item">
          <span>www.vemtragroup.com</span>
          <svg class="contact-icon" viewBox="0 0 22 22" aria-label="Website">
            <rect class="tile" width="22" height="22"/>
            <circle class="glyph" cx="11" cy="11" r="7"/>
            <path class="glyph-line" d="M4 11 H18 M11 4 Q7 11 11 18 M11 4 Q15 11 11 18"/>
          </svg>
        </li>
        <li class="contact-list__item">
          <span>2400 Larkspur Ave Suite 300 Marlow, GA 30412</span>
          <svg class="contact-icon" viewBox="0 0 22 22" aria-label="Address">
            <rect class="tile" width="22" height="22"/>
            <path class="glyph" d="M11 19 L6.5 11 A5 5 0 1 1 15.5 11 Z"/>
            <circle class="tile" cx="11" cy="8.5" r="1.8"/>
          </svg>
        </li>
      </ul>
    </div>
  </section>

  <section class="card-slot card-slot--back" aria-label="Card back">
    <div class="card">
      <span class="brand-dot brand-dot--back"></span>
      <div class="brand-name brand-name--back">Vemtra Group</div>
    </div>
  </section>

</main>
</body>
</html>
```